Rimo Application for Cars Accidents Services

We need app screen designs for company provide services for the cars that got accidents, the design should be modern official and simple, the pages around 26 include login, register, auth code, home, splash, request service, profile, settings, booking, booking info ..., we need something so professional please.

Target Market(s)

Cars owners

```html
<!DOCTYPE html>
<html lang="en">
<head>
<meta charset="utf-8">
<title>Rimo – App Screens</title>
<link rel="stylesheet" href="https://fonts.googleapis.com/css2?family=Montserrat:wght@400;500;600;800&display=swap">
<style>
  :root {
    --bg: #e0e8e3;
    --card: #ffffff;
    --ink: #121820;
    --muted: #8a8f96;
    --field: #f3f6f9;
    --green: #5a8a22;
    --green-light: #d8efc0;
    --splash-shade: #f7f7f7;
    --art-warm: #f2b54a;
    --art-cool: #f7e7c8;
  }
  * { box-sizing: border-box; margin: 0; padding: 0; }
  html, body { width: 1200px; height: 1200px; overflow: hidden; }
  body {
    background: var(--bg);
    font-family: "Montserrat", sans-serif;
    color: var(--ink);
    position: relative;
  }
  .brand-hero {
    position: absolute; left: 0; top: 100px; width: 1200px;
    text-align: center; font-weight: 800; font-size: 110px;
    letter-spacing: 2px; line-height: 1;
  }
  .screen {
    position: absolute; top: 296px; width: 224px; height: 485px;
    background: var(--card); border-radius: 19px; overflow: hidden;
  }
  .screen--splash { left: 87px; }
  .screen--signin { left: 354px; }
  .screen--signup { left: 621px; height: 606px; }
  .screen--intro { left: 888px; }
  .screen > * { position: absolute; }
  .splash-shade { left: 0; top: 0; width: 224px; height: 485px; }
  .brand-mark {
    left: 0; width: 100%; text-align: center; font-weight: 800;
    font-size: 34px; line-height: 1;
  }
  .back-btn {
    left: 12px; top: 24px; width: 28px; height: 28px; border-radius: 50%;
    background: var(--field); display: flex; align-items: center; justify-content: center;
  }
  .title { left: 0; width: 100%; text-align: center; font-size: 15px; font-weight: 600; }
  .subtitle { left: 0; width: 100%; text-align: center; font-size: 9.5px; }
  .label { left: 12px; font-size: 9.5px; }
  .field {
    left: 12px; width: 200px; height: 36px; border-radius: 6px; background: var(--field);
    font-size: 9.5px; color: var(--muted); padding-left: 14px;
    display: flex; align-items: center;
  }
  .field--secret { letter-spacing: 3px; font-size: 11px; color: #6b7076; }
  .field .eye { position: absolute; right: 14px; top: 11px; }
  .remember { left: 12px; top: 352px; display: flex; align-items: center; gap: 8px; font-size: 8.5px; }
  .checkbox { width: 12px; height: 12px; border: 1.3px solid var(--ink); border-radius: 2px; }
  .forgot { right: 12px; top: 353px; font-size: 8.5px; text-decoration: underline; }
  .btn {
    left: 12px; width: 200px; height: 36px; border-radius: 6px; background: var(--green);
    color: #fff; font-size: 10px; font-weight: 500;
    display: flex; align-items: center; justify-content: center;
  }
  .footer-note { left: 0; width: 100%; text-align: center; font-size: 9.5px; }
  .footer-note a { color: var(--green); text-decoration: underline; }
  .intro-art {
    left: 12px; top: 83px; width: 200px; height: 146px; border-radius: 10px;
    background: radial-gradient(circle at 45% 45%, var(--art-warm), var(--art-cool) 70%, #fff);
  }
  .intro-heading { left: 0; width: 100%; top: 280px; text-align: center; font-size: 15px; line-height: 18px; font-weight: 500; }
  .intro-body { left: 24px; width: 176px; top: 330px; text-align: center; font-size: 9.5px; line-height: 12px; color: var(--muted); }
  .dots { left: 0; width: 100%; top: 391px; display: flex; justify-content: center; gap: 7px; }
  .dot { width: 6px; height: 6px; border-radius: 50%; background: var(--green-light); }
  .dot--active { background: var(--green); }
</style>
</head>
<body>
  <div class="brand-hero">Rimo</div>

  <section class="screen screen--splash">
    <svg class="splash-shade" viewBox="0 0 224 485" aria-hidden="true">
      <polygon points="0,0 224,0 224,485 216,485 0,10" fill="var(--splash-shade)"/>
    </svg>
    <div class="brand-mark" style="top:226px">Rimo</div>
  </section>

  <section class="screen screen--signin">
    <div class="back-btn"><svg width="10" height="10" viewBox="0 0 10 10"><path d="M6.5 1.5 3 5l3.5 3.5" fill="none" stroke="var(--ink)" stroke-width="1.2" stroke-linecap="round"/></svg></div>
    <div class="brand-mark" style="top:92px">Rimo</div>
    <h1 class="title" style="top:157px">Sign In</h1>
    <p class="subtitle" style="top:182px">Please sign in your acoount</p>
    <span class="label" style="top:208px">Email address</span>
    <div class="field" style="top:230px">name1234@example.com</div>
    <span class="label" style="top:278px">Password</span>
    <div class="field field--secret" style="top:299px">•••••••
      <svg class="eye" width="14" height="14" viewBox="0 0 14 14"><path d="M1 7s2.4-4 6-4 6 4 6 4-2.4 4-6 4-6-4-6-4z" fill="none" stroke="var(--ink)" stroke-width="1.1"/><circle cx="7" cy="7" r="1.8" fill="none" stroke="var(--ink)" stroke-width="1.1"/></svg>
    </div>
    <label class="remember"><span class="checkbox"></span>Remember me</label>
    <span class="forgot">Forgot Password</span>
    <div class="btn" style="top:382px">Sign In</div>
    <p class="footer-note" style="top:437px">Don,t have an acccount? <a>Sign Up</a></p>
  </section>

  <section class="screen screen--signup">
    <div class="back-btn"><svg width="10" height="10" viewBox="0 0 10 10"><path d="M6.5 1.5 3 5l3.5 3.5" fill="none" stroke="var(--ink)" stroke-width="1.2" stroke-linecap="round"/></svg></div>
    <div class="brand-mark" style="top:92px">Rimo</div>
    <h1 class="title" style="top:157px">Sign Up</h1>
    <p class="subtitle" style="top:182px">Please sign up your acoount</p>
    <span class="label" style="top:214px">Name</span>
    <div class="field" style="top:235px">Daren Holt</div>
    <span class="label" style="top:291px">Email address</span>
    <div class="field" style="top:312px">name1234@example.com</div>
    <span class="label" style="top:360px">Password</span>
    <div class="field field--secret" style="top:382px">•••••••
      <svg class="eye" width="14" height="14" viewBox="0 0 14 14"><path d="M1 7s2.4-4 6-4 6 4 6 4-2.4 4-6 4-6-4-6-4z" fill="none" stroke="var(--ink)" stroke-width="1.1"/><circle cx="7" cy="7" r="1.8" fill="none" stroke="var(--ink)" stroke-width="1.1"/></svg>
    </div>
    <span class="label" style="top:430px">Password</span>
    <div class="field field--secret" style="top:451px">•••••••
      <svg class="eye" width="14" height="14" viewBox="0 0 14 14"><path d="M1 7s2.4-4 6-4 6 4 6 4-2.4 4-6 4-6-4-6-4z" fill="none" stroke="var(--ink)" stroke-width="1.1"/><circle cx="7" cy="7" r="1.8" fill="none" stroke="var(--ink)" stroke-width="1.1"/></svg>
    </div>
    <div class="btn" style="top:506px">Sign Up</div>
    <p class="footer-note" style="top:562px">Don,t have an acccount? <a>Sign In</a></p>
  </section>

  <section class="screen screen--intro">
    <div class="intro-art" role="img" aria-label="Illustration of two crashed yellow cars on fire with a worried driver beside them"></div>
    <h2 class="intro-heading">If your cars has an<br>accidents, Call us now</h2>
    <p class="intro-body">We will try to save you very soon, please if your has an accidents, than quickly call us</p>
    <div class="dots"><span class="dot dot--active"></span><span class="dot"></span><span class="dot"></span></div>
    <div class="btn" style="top:411px">Get Started</div>
  </section>
</body>
</html>
```